Visitenkarten-Design für Immobilien-Unternehmen
Designer ist sehr bemüht und die Änderungswünsche wurden rasch bearbeitet. Auch wurde im Nachhinein noch mein Wunsch auf Adaptierung zu einem Lackdruck bearbeitet und gesendet. Ich bin mit der Abwicklung vollkommen zufrieden - Vielen Dank
Zielgruppe
Die TOLU Immobilien GmbH ist eine durch Ing. Kilian Frühwald inhabergeführte Gesellschaft, welche sich schwerpunktmäßig mit Immobilieninvestitionen sowie Beteiligungen im Bereich von Wohn- und Gewerbeimmobilien beschäftigt. Das Unternehmen kauft, hält, vermietet und verkauft Liegenschaften aller Art, mit dem Fokus auf Gewerbe- und Wohnimmobilien. Zielgruppe sind Personen, welche Immobilien verkaufen möchten - wir betreiben nur eigene Vermögensverwaltung
siehe: www.tolu-immobilien.at
Aufgabenstellung
schlicht und einfach gehalten - weniger ist mehr - nur die wichtigsten Informationen auf der Visitenkarte.
siehe Homepage: www.tolu-immobilien.at

```html
<!DOCTYPE html>
<html lang="de">
<head>
<meta charset="utf-8">
<title>TOLU Immobilien GmbH – Visitenkarte</title>
<link href="https://fonts.googleapis.com/css2?family=Roboto:wght@300&display=swap" rel="stylesheet">
<style>
  :root {
    --paper: #ffffff;
    --ink: #1d1d1b;
    --ink-soft: #3a3a3a;
    --band-grey: #9d9d9c;
    --shadow: rgba(0, 0, 0, 0.45);
  }
  * { box-sizing: border-box; margin: 0; padding: 0; }
  html, body {
    width: 1200px; height: 1200px; overflow: hidden;
    background: var(--paper);
    font-family: "Roboto", Arial, sans-serif;
    font-weight: 300;
  }
  .canvas { position: relative; width: 1200px; height: 1200px; }
  .card {
    position: absolute; left: 318px; width: 567px; height: 324px;
    box-shadow: 7px 8px 9px var(--shadow);
    overflow: hidden;
  }
  .card--front { top: 198px; background: var(--paper); }
  .card--back { top: 675px; background: var(--ink); }

  .wordmark { position: absolute; color: var(--ink); line-height: 1; }
  .wordmark__name { display: block; font-size: 66px; letter-spacing: 1px; }
  .wordmark__sub { display: block; font-size: 19px; letter-spacing: 1.5px; margin-top: 10px; }
  .card--front .wordmark { left: 34px; top: 36px; }
  .card--back .wordmark {
    left: 0; right: 0; top: 112px; text-align: center; color: var(--paper);
  }

  .holder { position: absolute; left: 40px; top: 190px; color: var(--ink-soft); font-size: 22px; line-height: 27px; }
  .contact {
    position: absolute; right: 49px; text-align: right; font-style: normal;
    color: var(--ink-soft); font-size: 17px; line-height: 22px;
  }
  .contact--address { top: 118px; }
  .contact--reach { top: 196px; }

  .band { position: absolute; left: 0; bottom: 0; height: 46px; }
  .band--dark { width: 276px; background: var(--ink); }
  .band--light { left: 276px; width: 291px; background: var(--band-grey); }
</style>
</head>
<body>
<main class="canvas">
  <section class="card card--front" aria-label="Vorderseite">
    <div class="wordmark">
      <span class="wordmark__name">TOLU</span>
      <span class="wordmark__sub">IMMOBILIEN GMBH</span>
    </div>
    <div class="holder">
      <p>Your Name</p>
      <p>Your Position</p>
    </div>
    <address class="contact contact--address">
      Ahornweg 42/5<br>8211 Ilztal<br>Austria
    </address>
    <div class="contact contact--reach">
      office@tolu-immobilien.at<br>+43 664 482 17 35
    </div>
    <div class="band band--dark"></div>
    <div class="band band--light"></div>
  </section>

  <section class="card card--back" aria-label="Rückseite">
    <div class="wordmark">
      <span class="wordmark__name">TOLU</span>
      <span class="wordmark__sub">IMMOBILIEN GMBH</span>
    </div>
  </section>
</main>
</body>
</html>
```